Zielgruppe
Wir sind ein Vertriebsunternehmen, mit dem Ziel die klassische Finanz und den Kryptosektor zu verbinden. Unsere Zielgruppe sind Menschen zwischn 25 - 45 Jahre. Wir sind die Communty und Vertrieb der ersten rechtkonformen STO - Plattform ( Plattform für Wertpapiere im Kryptosektor)
Diese Projekt ist Teil eines Paketes, wir bitten nur Designer mit zu machen die alle benötigten Unterlagen designen können. (siehe restliche Projekte) - Gesamtvolumen: 2300€ Preisgeld
Online-Marketing Material
2 Vorlagen Social Media - (Einladung/Event, Sprüche/Information)
Banner
Präsentationsvorlagen - min unterschiedliche 8 Vorlagenseiten /Layouts.
Landingpage Layout f. Funnelsite für Webinaranmeldung mit Platz für Formular
Newsletter Layoutvorlage
Vorlage Infografik
Broschüre / E - Book Designe
Es werden nur Vorlagen benötigt mit 'LoremSum Texten' und Musterbildern. Wir möchten von allen Vorlagen die Originaldatei, uns stehen folgende Grafikprogramme zur Verfügung:
Adobe Photoshop
Adobe Illustrator
Canva
Newsletter und Landingpage Software: postflinkel.com
Unsere Akt. Designe (Designe Alt) gefällt uns von der Idee, dennoch wünschen wir es uns moderner und edler mit ein wenig 'spaceig'. - Eben die Vereinigung von Kryptowelt und klassischer Finanz.
Schriftart: Poppins
Farben lt. Logo
Aufgabenstellung
Diese Projekt ist Teil eines Paketes, wir bitten nur Designer mit zu machen die alle benötigten Unterlagen designen können. (siehe restliche Projekte) - Gesamtvolumen: 2000€ - 2300€ Preisgeld

```html
<!DOCTYPE html>
<html lang="de">
<head>
<meta charset="utf-8">
<title>Talvera – Zitat Vorlage</title>
<link href="https://fonts.googleapis.com/css2?family=Poppins:wght@400;500;700&display=swap" rel="stylesheet">
<style>
  :root {
    --page-bg: #e6e6ef;
    --card-blue: #1f55a5;
    --card-blue-deep: #174a96;
    --card-blue-light: #2a63b3;
    --white: #ffffff;
    --quote-white: #eef0f7;
    --brand-blue: #1f4ea3;
    --band: #eceef6;
    --photo-tone: #4f78b8;
    --tagline-grey: #3a4a66;
  }
  * { margin: 0; padding: 0; box-sizing: border-box; }
  html, body { width: 1200px; height: 1199px; overflow: hidden; background: var(--page-bg); }
  body { font-family: "Poppins", sans-serif; position: relative; }

  .quote-card {
    position: absolute; left: 44px; top: 150px; width: 1113px; height: 1007px;
    border-radius: 24px; overflow: hidden;
    background: radial-gradient(ellipse at 65% 25%, var(--card-blue-light) 0%, var(--card-blue) 50%, var(--card-blue-deep) 100%);
  }
  .portrait {
    position: absolute; left: 764px; top: 591px; width: 370px; height: 370px; border-radius: 50%;
    background: radial-gradient(circle at 50% 40%, #8aa5d4 0%, var(--photo-tone) 65%, #3d66ab 100%);
  }
  .footer-band {
    position: absolute; left: 0; top: 897px; width: 100%; height: 56px; background: var(--band);
  }

  .brand-badge {
    position: absolute; left: 455px; top: 40px; width: 290px; height: 298px;
    background: var(--page-bg); border-radius: 48px;
  }
  .brand-badge-inner {
    position: absolute; left: 26px; top: 28px; width: 238px; height: 242px;
    background: var(--white); border-radius: 36px;
    display: flex; flex-direction: column; align-items: center; justify-content: center; gap: 14px;
  }
  .brand-badge-dot { width: 56px; height: 56px; border-radius: 50%; background: var(--brand-blue); }
  .brand-badge-name { font-weight: 500; font-size: 28px; color: var(--brand-blue); }

  .quote-mark { position: absolute; left: 116px; top: 237px; width: 132px; height: 111px; }
  .quote-mark path { fill: var(--quote-white); }

  .quote-text {
    position: absolute; left: 116px; top: 382px; width: 990px;
    color: var(--white); font-size: 38.5px; line-height: 56px; font-weight: 400;
  }
  .quote-author {
    position: absolute; left: 116px; top: 748px; color: var(--white);
    font-weight: 700; font-size: 37px;
  }
  .quote-role {
    position: absolute; left: 116px; top: 808px; color: var(--white);
    font-weight: 400; font-size: 37px;
  }

  .footer-card {
    position: absolute; left: 82px; top: 1012px; width: 586px; height: 127px;
    background: var(--white); border-radius: 12px;
    box-shadow: 0 4px 14px rgba(20, 40, 90, 0.18);
    padding: 22px 0 0 39px;
  }
  .footer-brand { display: flex; align-items: center; gap: 11px; }
  .footer-brand-mark { width: 50px; height: 50px; background: var(--brand-blue); border-radius: 6px; flex: none; }
  .footer-brand-name { font-weight: 500; font-size: 29px; line-height: 32px; color: var(--brand-blue); }
  .footer-tagline { font-size: 14px; letter-spacing: 2.3px; color: var(--tagline-grey); line-height: 18px; white-space: nowrap; }
  .footer-copyright { margin-top: 8px; font-size: 17.5px; color: var(--brand-blue); white-space: nowrap; }
</style>
</head>
<body>
  <section class="quote-card">
    <div class="portrait" role="img" aria-label="Foto einer lächelnden Person mit Laptop"></div>
    <div class="footer-band"></div>
  </section>

  <div class="brand-badge">
    <div class="brand-badge-inner">
      <div class="brand-badge-dot"></div>
      <div class="brand-badge-name">Talvera</div>
    </div>
  </div>

  <svg class="quote-mark" viewBox="0 0 132 111" aria-hidden="true">
    <path d="M0,111 L0,60 Q6,14 52,0 L58,14 Q36,28 33,52 L60,52 L60,111 Z"/>
    <path d="M72,111 L72,60 Q78,14 124,0 L130,14 Q108,28 105,52 L132,52 L132,111 Z"/>
  </svg>

  <p class="quote-text">“Muster Zitat/Spruch text Lorem ipsum dolor amet consetetur sadipscing elitr sed diam nonumy eieil mod tempor invidu labore et dolore magna aliqu sadipscing elitr, sed diam nonumy eirmod tempor est yam erat, sed diam voluptua est vero eoetabc usam et justo duo dolores etea rebum.“</p>
  <p class="quote-author">Muster Person</p>
  <p class="quote-role">Muster Titel/Position</p>

  <footer class="footer-card">
    <div class="footer-brand">
      <div class="footer-brand-mark"></div>
      <div>
        <div class="footer-brand-name">Talvera Investments</div>
        <div class="footer-tagline">KLAR UND BEWUSST IN FIRMENWERTE ANLEGEN</div>
      </div>
    </div>
    <div class="footer-copyright">© 2023 Talvera Investments. Alle Rechte vorbehalten</div>
  </footer>
</body>
</html>
```